Business Cards - Brightway Harbor

need to design unique business card for my mortgage business. I need to design credit card style business card for my business or any unique idea that you might have

Target Market(s)

Home Loan customers

Industry/Entity Type

Mortgage Brokerage

Contact Information for Business Card

please design credit card style or very unique style business card

Colors

Designer to choose colors to be used in the design.

Requirements
Must have
• Name
• position
• Phone number
• fax number
• email address
• website address
• social media address
• All above fields will be provided once design in finalised

```html
<!DOCTYPE html>
<html lang="en">
<head>
<meta charset="utf-8">
<title>Brightway Harbor – Business Card</title>
<link rel="stylesheet" href="https://fonts.googleapis.com/css2?family=Exo+2:wght@500;600;700&display=swap">
<style>
  :root{
    --backdrop:#a6c4cd;
    --card-blue:#44607e;
    --chip-blue:#4e6b8c;
    --paper:#ffffff;
    --ink:#2f4a66;
    --brand-blue:#1f3fa6;
    --shadow:rgba(40,60,80,.35);
  }
  html,body{margin:0;padding:0;overflow:hidden}
  body{
    width:1200px;height:1200px;position:relative;
    background:var(--backdrop);
    font-family:"Exo 2",sans-serif;
  }
  .card{
    position:absolute;border-radius:30px;overflow:hidden;
    box-shadow:6px 12px 18px var(--shadow);
  }
  .card--front{left:243px;top:75px;width:781px;height:478px;background:var(--card-blue)}
  .card--back{left:243px;top:649px;width:768px;height:476px;background:var(--paper)}

  .stripe{position:absolute;left:0;top:49px;width:100%;height:125px;background:var(--paper)}

  .front-brand{
    position:absolute;left:0;right:0;top:265px;text-align:center;color:var(--paper);
  }
  .front-brand__name{
    display:inline-flex;align-items:center;gap:16px;
    font-weight:600;font-size:52px;letter-spacing:1px;line-height:1;
  }
  .front-brand__dot{width:22px;height:22px;border-radius:50%;background:var(--paper)}

  .chip{position:absolute;left:67px;top:133px;width:114px;height:103px}
  .slot-arrow{position:absolute;left:33px;top:172px;width:15px;height:29px}

  .contact{
    position:absolute;right:40px;top:133px;margin:0;padding:0;list-style:none;
    text-align:right;color:var(--ink);font-weight:700;font-size:17px;
    letter-spacing:1px;line-height:27px;text-transform:uppercase;
  }
  .person{position:absolute;left:54px;top:296px;color:var(--ink)}
  .person__phone{font-weight:700;font-size:16px;letter-spacing:.5px;text-transform:uppercase}
  .person__name{font-weight:500;font-size:42px;margin-top:18px;line-height:1}
  .person__position{font-weight:700;font-size:26px;letter-spacing:1px;margin-top:10px;text-transform:uppercase}

  .back-brand{position:absolute;right:42px;bottom:56px;text-align:right}
  .back-brand__name{
    display:inline-flex;align-items:center;gap:10px;
    color:var(--brand-blue);font-weight:600;font-size:30px;line-height:1;
  }
  .back-brand__square{width:14px;height:14px;background:var(--brand-blue)}
</style>
</head>
<body>
  <section class="card card--front">
    <div class="stripe"></div>
    <div class="front-brand">
      <span class="front-brand__name"><span class="front-brand__dot"></span>Brightway Harbor</span>
    </div>
  </section>

  <section class="card card--back">
    <svg class="slot-arrow" viewBox="0 0 15 29"><polygon points="15,0 15,29 0,14.5" fill="var(--card-blue)"/></svg>
    <svg class="chip" viewBox="0 0 114 103">
      <rect width="114" height="103" rx="18" fill="var(--chip-blue)"/>
      <g stroke="var(--paper)" stroke-width="4" fill="none">
        <line x1="0" y1="30" x2="38" y2="30"/>
        <line x1="0" y1="52" x2="38" y2="52"/>
        <line x1="0" y1="74" x2="38" y2="74"/>
        <line x1="76" y1="30" x2="114" y2="30"/>
        <line x1="76" y1="52" x2="114" y2="52"/>
        <line x1="76" y1="74" x2="114" y2="74"/>
        <polyline points="38,0 38,18 76,18 76,103"/>
        <line x1="38" y1="30" x2="38" y2="103"/>
      </g>
    </svg>

    <ul class="contact">
      <li>Website Address</li>
      <li>Fax Number</li>
      <li>Email Address</li>
      <li>Social Media Address</li>
    </ul>

    <div class="person">
      <div class="person__phone">Phone Number</div>
      <div class="person__name">Name</div>
      <div class="person__position">Position</div>
    </div>

    <div class="back-brand">
      <span class="back-brand__name"><span class="back-brand__square"></span>Brightway Harbor</span>
    </div>
  </section>
</body>
</html>
```